Rising Paths Web Design

I am starting a new company that will provide LIFE COACHING services - I have tried to design a website, but it's too complicated. Right now, it's just me - I'm the only person that will provide services through the website - I have used artmarket to purchase a logo (see below). I want to be able to update the website myself, but need a template - basic design. Because I am not technologically savvy enough to explain in words - I basically want to have a website that will provide basic information about my services (coaching), a page about me and my background, hopefully scheduling possibilities, and testimonials — also a page for writing/blogs. I bought a website through NetHarbor - so when I have a template, I guess I”d use that - but maybe I’ll need to work with a designer to actually get it up on the internet. I have a head shot that I’ll upload, too.
Target Market(s)
Clients from the independent (private school) world - teachers, administrators
Number of Pages Required
4 page
Look and feel
Each slider illustrates characteristics of the customer's brand and the style your logo design should communicate.

```html
<!DOCTYPE html>
<html lang="en">
<head>
<meta charset="utf-8">
<title>Rising Paths – Life Coaching</title>
<link rel="stylesheet" href="https://fonts.googleapis.com/css2?family=Montserrat:wght@400;500;600;700&family=Great+Vibes&display=swap">
<style>
:root{
  --teal:#1ba58e;
  --teal-dark:#148873;
  --teal-deep:#0f6f5f;
  --mint:#e3f5f1;
  --mint-2:#cdeee7;
  --pink:#ef2f6b;
  --ink:#2f3b3a;
  --muted:#6b7a78;
  --white:#ffffff;
  --leaf-1:#6f9a3c;
  --leaf-2:#b8d27a;
}
*{box-sizing:border-box;margin:0;padding:0}
html,body{width:1200px;height:2624px;overflow:hidden}
body{font-family:"Montserrat",Arial,sans-serif;color:var(--ink);background:var(--white);font-size:14px;line-height:1.6}
.script{font-family:"Great Vibes",cursive;font-weight:400}
.btn{display:inline-block;background:var(--pink);color:var(--white);font-size:12px;font-weight:600;padding:10px 24px;border-radius:2px;text-decoration:none;letter-spacing:.5px}
.photo{display:block}

/* header */
.site-header{height:70px;display:flex;align-items:center;justify-content:space-between;padding:0 60px;background:var(--white);border-bottom:1px solid #e6eceb}
.brand{display:flex;align-items:center;gap:10px;font-weight:600;font-size:18px;color:var(--teal)}
.brand-dot{width:22px;height:22px;border-radius:50%;background:var(--teal)}
.main-nav{display:flex;gap:30px;font-size:13px;font-weight:500}
.main-nav a{color:var(--ink);text-decoration:none}
.social{display:flex;gap:8px}
.social span{width:20px;height:20px;border-radius:50%;background:#4a5554}

/* hero */
.hero{position:relative;height:400px;background:radial-gradient(ellipse at 50% 0%,var(--leaf-2) 0%,var(--leaf-1) 55%,#3f6b2a 100%)}
.hero-card{position:absolute;left:80px;top:40px;width:330px;height:320px;background:rgba(255,255,255,.95);padding:34px 34px;display:flex;flex-direction:column;gap:10px}
.hero-card .brand{font-size:20px}
.hero-card h1{font-size:26px;font-weight:600;margin-top:14px}
.hero-card .byline{font-size:12px;color:var(--muted)}
.hero-card .tagline{font-size:34px;color:var(--teal);line-height:1.1;margin:6px 0 10px}
.hero-card .btn{align-self:flex-start}

/* about */
.about{height:330px;background:var(--mint);display:flex;align-items:center;gap:50px;padding:0 160px}
.about .portrait{width:280px;height:240px;background:linear-gradient(160deg,#f3e3c7,#c9b58f);flex:none}
.about-text h2{font-size:38px;color:var(--pink);line-height:1}
.about-text .name{font-size:13px;font-weight:600;margin:4px 0 12px}
.about-text p{font-size:13px;color:var(--muted);margin-bottom:10px}
.about-foot{display:flex;align-items:center;gap:14px;margin-top:8px}
.badge{width:30px;height:22px;background:#b9c7c5;border-radius:3px}

/* services */
.services{height:460px;background:var(--teal);color:var(--white);text-align:center;padding-top:40px}
.services h2{font-size:28px;font-weight:600;letter-spacing:3px}
.services .sub{font-size:13px;opacity:.9;margin-bottom:26px}
.service-list{display:flex;justify-content:center;gap:30px;margin-bottom:26px}
.service-card{width:240px;height:250px;position:relative;border:3px solid var(--white);background:linear-gradient(160deg,#8aa3a0,#3d5552)}
.service-card h3{position:absolute;left:0;right:0;top:0;padding:8px;font-size:13px;font-weight:600;background:rgba(15,111,95,.85);line-height:1.3}

/* blog */
.blog{height:380px;background:var(--mint);padding-top:30px}
.blog h2{text-align:center;font-size:40px;color:var(--teal-dark);line-height:1;margin-bottom:24px}
.blog-row{display:flex;gap:44px;padding:0 220px;align-items:flex-start}
.blog-row .photo{width:320px;height:240px;background:linear-gradient(150deg,#d7e4ec,#7f9fb4);flex:none}
.blog-text h3{font-size:15px;font-weight:600;line-height:1.4;margin:10px 0 14px;text-transform:uppercase}
.blog-text p{font-size:13px;color:var(--muted);margin-bottom:10px}
.blog-text .more{color:var(--teal);font-size:12px;display:block;margin:14px 0 12px}

/* newsletter */
.newsletter{height:300px;background:var(--mint-2);display:flex;align-items:center;justify-content:center;gap:60px}
.subscribe{width:320px;background:var(--white);padding:26px;text-align:center}
.subscribe h2{font-size:30px;color:var(--teal-dark);line-height:1.1}
.subscribe p{font-size:12px;color:var(--muted);margin:6px 0 14px}
.field{height:30px;border:1px solid #cfdbd9;margin-bottom:8px;text-align:left;font-size:11px;color:#9aa8a6;padding:6px 10px}
.subscribe .btn{background:var(--teal-dark);width:100%;margin-top:6px}
.newsletter .photo{width:340px;height:230px;background:linear-gradient(140deg,#f4eee8,#d9cfc6)}

/* testimonials */
.testimonials{height:320px;background:var(--teal);color:var(--white);text-align:center;padding-top:40px;position:relative}
.quote-mark{position:absolute;left:150px;top:20px;font-size:130px;line-height:1;opacity:.2;font-family:Georgia,serif}
.testimonials h2{font-size:40px;line-height:1;margin-bottom:30px}
.people{display:flex;justify-content:center;align-items:center;gap:80px}
.arrow{width:30px;height:30px}
.person{width:160px}
.avatar{width:80px;height:80px;border-radius:50%;margin:0 auto 12px;border:3px solid var(--white);background:linear-gradient(160deg,#e9c9a8,#a77d5a)}
.person strong{display:block;font-size:14px;font-weight:600}
.person span{font-size:11px;opacity:.85}

/* cta */
.cta{height:224px;background:linear-gradient(180deg,#cfe3a6 0%,var(--leaf-1) 60%,#45722d 100%);display:flex;flex-direction:column;align-items:center;justify-content:center;gap:14px}
.cta h2{font-size:26px;font-weight:600;color:var(--white)}
.cta .btn{background:var(--teal-dark)}

/* footer */
.site-footer{height:50px;background:var(--teal-deep);color:var(--white);font-size:11px;display:flex;align-items:center;justify-content:center}
.footer-brand{height:70px;display:flex;align-items:center;justify-content:center}
</style>
</head>
<body>

<header class="site-header">
  <div class="brand"><span class="brand-dot"></span>Rising Paths</div>
  <nav class="main-nav">
    <a href="#">Home</a><a href="#">About Me</a><a href="#">My Services</a><a href="#">Blog</a><a href="#">Contact</a>
  </nav>
  <div class="social"><span></span><span></span><span></span><span></span></div>
</header>

<section class="hero" role="img" aria-label="Photo looking up into a green forest canopy">
  <div class="hero-card">
    <div class="brand"><span class="brand-dot"></span>Rising Paths</div>
    <h1>Life Coaching</h1>
    <div class="byline">By Dana Whitfield</div>
    <div class="tagline script">Grow &amp; live your life with purpose</div>
    <a class="btn" href="#">Find out more</a>
  </div>
</section>

<section class="about">
  <div class="portrait photo" role="img" aria-label="Head shot of the coach"></div>
  <div class="about-text">
    <h2 class="script">Hi there!</h2>
    <div class="name">I'm Dana Whitfield</div>
    <p>I help teachers and school leaders find clarity, balance and direction so they can build careers and lives that feel right.</p>
    <p>Together we set goals, build habits and move forward one step at a time.</p>
    <div class="about-foot">
      <a class="btn" href="#">Get to know me</a>
      <span class="badge"></span><span class="badge"></span><span class="badge"></span>
    </div>
  </div>
</section>

<section class="services">
  <h2>SERVICES</h2>
  <p class="sub">Check out what we have to offer to help you grow</p>
  <div class="service-list">
    <div class="service-card" role="img" aria-label="Photo of a one-on-one coaching session"><h3>One-on-one<br>Life Coaching</h3></div>
    <div class="service-card" role="img" aria-label="Photo of a seminar group"><h3>Seminars</h3></div>
    <div class="service-card" role="img" aria-label="Photo of a consultation at a laptop"><h3>Consultation</h3></div>
  </div>
  <a class="btn" href="#">Schedule an appointment</a>
</section>

<section class="blog">
  <h2 class="script">Our Latest Blog Post</h2>
  <div class="blog-row">
    <div class="photo" role="img" aria-label="Photo of colleagues shaking hands in an office"></div>
    <div class="blog-text">
      <h3>Five essential things you must do to grow your career</h3>
      <p>Simple steps can change the way you work and lead. Here are five habits that help educators grow with confidence.</p>
      <p>Start small, stay curious and keep your purpose close.</p>
      <span class="more">Read More</span>
      <a class="btn" href="#">Visit Blog</a>
    </div>
  </div>
</section>

<section class="newsletter">
  <div class="subscribe">
    <h2 class="script">Subscribe to our newsletter</h2>
    <p>Get our weekly insights into life and career growth</p>
    <div class="field">Name</div>
    <div class="field">Email address</div>
    <a class="btn" href="#">Subscribe</a>
  </div>
  <div class="photo" role="img" aria-label="Photo of a laptop and coffee on a bed"></div>
</section>

<section class="testimonials">
  <div class="quote-mark">“</div>
  <h2 class="script">Testimonials</h2>
  <div class="people">
    <svg class="arrow" viewBox="0 0 30 30"><path d="M19 6 L10 15 L19 24" fill="none" stroke="#fff" stroke-width="3"/></svg>
    <div class="person"><div class="avatar" role="img" aria-label="Client portrait"></div><strong>Lena Marsh</strong><span>Teacher</span></div>
    <div class="person"><div class="avatar" role="img" aria-label="Client portrait"></div><strong>Owen Brooks</strong><span>Head of School</span></div>
    <div class="person"><div class="avatar" role="img" aria-label="Client portrait"></div><strong>Maya Ellis</strong><span>Administrator</span></div>
    <svg class="arrow" viewBox="0 0 30 30"><path d="M11 6 L20 15 L11 24" fill="none" stroke="#fff" stroke-width="3"/></svg>
  </div>
</section>

<section class="cta" role="img" aria-label="Photo of a forest canopy with a call to action">
  <h2>Ready to start growing?</h2>
  <a class="btn" href="#">Schedule an appointment</a>
</section>

<footer class="site-footer">© 2024 Rising Paths. All rights reserved.</footer>
<div class="footer-brand"><div class="brand"><span class="brand-dot"></span>Rising Paths</div></div>

</body>
</html>
```